Powerpoint and Word Document Template

Our target market are C-suite executives in banks, credit unions, non-bank financial institutions, financial technology companies and in the law firms, private equity firms and the like that are also advising the industry.

design should convey: confidence, trust, expertise, experience, value, advice, relationship focus.

For the stationery design, we will need the .doc format as well.

Industry/Entity Type

Consulting

Font styles to use
Sans Serif

Colors
0356a4
3277b5
85acd3
cedeed
eaf1f7
ffffff

Requirements
Must have
• must use the logo and color scheme included in the attached zip file. must include a powerpoint template with a cover slide, section break slides, slides for images/graphics, slides for side by side content, and slides for regular content.

Note: this should also include designs for word documents like stationary and envelopes based on the same concept.

```html
<!DOCTYPE html>
<html lang="en">
<head>
<meta charset="utf-8">
<title>Verant Advisory – Content Slide</title>
<link rel="stylesheet" href="https://fonts.googleapis.com/css2?family=Lato:wght@400;700;900&display=swap">
<style>
  :root {
    --navy: #034c8c;
    --amber: #fbb534;
    --amber-soft: #f7c15a;
    --gold: #d19d3b;
    --white: #ffffff;
    --photo-light: #e8e4dc;
    --photo-mid: #b9a890;
    --photo-dark: #3a3a3f;
  }
  * { margin: 0; padding: 0; box-sizing: border-box; }
  html, body {
    width: 1200px; height: 675px; overflow: hidden;
    background: var(--navy);
  }
  .slide {
    position: relative; width: 1200px; height: 675px;
    background: var(--navy); overflow: hidden;
    font-family: 'Lato', sans-serif; color: var(--white);
  }
  .slide-art { position: absolute; inset: 0; }
  .brand {
    position: absolute; left: 87px; top: 33px;
    display: flex; align-items: center; gap: 12px;
  }
  .brand-mark {
    width: 56px; height: 56px;
    border: 4px solid var(--white);
  }
  .brand-name {
    font-family: 'Lato', sans-serif; font-weight: 700;
    font-size: 27px; letter-spacing: 1px; line-height: 1;
    color: var(--white);
  }
  .headline {
    position: absolute; left: 87px; top: 155px;
    font-weight: 900; font-size: 41px; line-height: 45px;
    text-transform: uppercase; letter-spacing: -0.5px;
  }
  .headline .accent { color: var(--amber); }
  .points { position: absolute; left: 87px; top: 265px; width: 440px; }
  .point { margin-bottom: 25px; }
  .point-title { font-weight: 700; font-size: 12.5px; line-height: 18px; margin-bottom: 5px; }
  .point-body { font-weight: 400; font-size: 10.6px; line-height: 17.5px; }
</style>
</head>
<body>
<main class="slide">
  <svg class="slide-art" width="1200" height="675" viewBox="0 0 1200 675">
    <defs>
      <linearGradient id="photoTone" x1="0" y1="0" x2="1" y2="1">
        <stop offset="0" stop-color="var(--photo-light)"/>
        <stop offset="0.55" stop-color="var(--photo-mid)"/>
        <stop offset="1" stop-color="var(--photo-dark)"/>
      </linearGradient>
      <linearGradient id="amberTone" x1="0" y1="0" x2="1" y2="1">
        <stop offset="0" stop-color="var(--amber)"/>
        <stop offset="1" stop-color="var(--amber-soft)"/>
      </linearGradient>
    </defs>
    <polygon class="amber-panel" points="431,0 636,0 636,319" fill="url(#amberTone)"/>
    <polygon class="gold-edge" points="431,0 453,0 636,294 636,319" fill="var(--gold)"/>
    <polygon class="hero-photo" role="img"
      aria-label="Photo: business advisors reviewing financial charts on a clipboard beside a laptop"
      points="636,0 1200,0 1200,675 878,675 636,288" fill="url(#photoTone)"/>
  </svg>

  <div class="brand">
    <div class="brand-mark"></div>
    <div class="brand-name">VERANT ADVISORY</div>
  </div>

  <h1 class="headline">Lorem Ipsun <span class="accent">Dolor</span><br><span class="accent">Sit Amet</span></h1>

  <section class="points">
    <article class="point">
      <h2 class="point-title">Your title text one</h2>
      <p class="point-body">Lorem ipsum dolor sit amet, consectetur adipiscing elit, sed do eiusmod tempor incididunt ut labore et dolore magna aliqua.&nbsp; Quis ipsum suspendisse ultrices gravida. Risus commodo viverra maecenas accumsan lacus vel facilisis.</p>
    </article>
    <article class="point">
      <h2 class="point-title">Your title text one</h2>
      <p class="point-body">Lorem ipsum dolor sit amet, consectetur adipiscing elit, sed do eiusmod tempor incididunt ut labore et dolore magna aliqua.&nbsp; Quis ipsum suspendisse ultrices gravida. Risus commodo viverra maecenas accumsan lacus vel facilisis.</p>
    </article>
    <article class="point">
      <h2 class="point-title">Your title text one</h2>
      <p class="point-body">Lorem ipsum dolor sit amet, consectetur adipiscing elit, sed do eiusmod tempor incididunt ut labore et dolore magna aliqua.&nbsp; Quis ipsum suspendisse ultrices gravida. Risus commodo viverra maecenas accumsan lacus vel facilisis.</p>
    </article>
  </section>
</main>
</body>
</html>
```